Real Estate Sign Project

We need a Real Estate sign that promotes the property being listed and our company and agent listing the property. The images need to be able to be swapped out so we can use the template for each listing we have. I have a sample from another company that shows what were are trying to accomplish. Would want ours to be unique using our logo and the colors in our logo. We would like to not have to use a rider. Would want agents name and phone number to be part of the 36" x 24" sign.

Industry/Entity Type

Real Estate

Requirements
Must have
• Sign dimensions are 36 inches by 24 inches (36" across and 24" up down). Use example.of.sign.we.want.jpg as the direction we want to go but with a different layout and our logo and colors. This would be just a template that we can swap out new pictures, address, price, website, agents contact info for each home we are listing. Like the idea of the pictures bleeding off the sides. Please use free stock photos for the home images as we will be changing these out for each listing. Please incorporate all info including agents info into the one sign. File must be layered so we can change the pictures, price, website, agent, etc. We use GIMP (.xcf) file

```html
<!DOCTYPE html>
<html lang="en">
<head>
<meta charset="utf-8">
<title>Home For Sale – 1418 Larkspur Lane</title>
<link rel="stylesheet" href="https://fonts.googleapis.com/css2?family=Oswald:wght@500;600&family=Ubuntu:wght@400;500;700&display=swap">
<style>
  :root {
    --page: #2b2b2d;
    --card-top: #e4e6ee;
    --card-bottom: #cfd3df;
    --navy: #1f2a5c;
    --sky: #4a9bd6;
    --sky-light: #6cb5e6;
    --orange: #e2601d;
    --orange-light: #f39a3c;
    --white: #ffffff;
  }
  * { box-sizing: border-box; margin: 0; padding: 0; }
  html, body { width: 1200px; height: 900px; overflow: hidden; }
  body { background: var(--page); position: relative; font-family: "Ubuntu", sans-serif; }

  .sign {
    position: absolute; left: 60px; top: 90px; width: 1080px; height: 720px;
    background: linear-gradient(180deg, var(--card-top), var(--card-bottom));
    overflow: hidden;
  }
  .footer-band {
    position: absolute; left: 0; right: 0; top: 610px; bottom: 0;
    background: linear-gradient(180deg, var(--sky-light), var(--sky));
  }
  .website {
    position: absolute; left: 40px; top: 648px;
    font: 700 26px/1 "Ubuntu", sans-serif; color: var(--navy); letter-spacing: 0.5px;
  }
  .agent {
    position: absolute; right: 40px; top: 626px; text-align: right;
    color: var(--navy);
  }
  .agent-name { font: 700 24px/1.2 "Ubuntu", sans-serif; }
  .agent-phone { font: 500 26px/1.3 "Ubuntu", sans-serif; }
  .hero-photo {
    position: absolute; left: 0; top: 92px; width: 560px; height: 500px;
    border-radius: 0 26px 26px 0;
    background: linear-gradient(180deg, #8fb7e3 0%, #c9dbef 30%, #4f5e52 55%, #5f8f3a 78%, #c4c2bc 100%);
    box-shadow: 4px 4px 12px rgba(0,0,0,0.35);
  }
  .sale-label {
    position: absolute; left: 610px; width: 330px; top: 28px; text-align: center;
    font: 500 20px/1 "Ubuntu", sans-serif; color: var(--navy);
  }
  .price {
    position: absolute; left: 610px; width: 330px; top: 52px; text-align: center;
    font: 600 46px/1.1 "Oswald", sans-serif; color: var(--orange);
  }
  .headline-band {
    position: absolute; left: 560px; right: 0; top: 120px; height: 56px;
    background: var(--sky-light);
  }
  .headline {
    position: absolute; left: 588px; top: 130px;
    font: 500 32px/1.1 "Ubuntu", sans-serif; color: var(--navy);
  }
  .thumbs { position: absolute; left: 592px; top: 186px; display: flex; gap: 14px; }
  .thumb {
    width: 146px; height: 102px; border-radius: 12px;
    border: 3px solid var(--white);
    box-shadow: 2px 3px 8px rgba(0,0,0,0.35);
  }
  .thumb--living { background: linear-gradient(160deg, #d9c79a, #8a7a5a); }
  .thumb--bedroom { background: linear-gradient(160deg, #e6d6b8, #a58c66); }
  .thumb--bath { background: linear-gradient(160deg, #e4e2dc, #9b9288); }
  .address-band {
    position: absolute; left: 560px; right: 30px; top: 302px; height: 60px;
    background: linear-gradient(180deg, var(--orange-light), var(--orange));
  }
  .address {
    position: absolute; left: 586px; top: 306px;
    font: 600 36px/1.4 "Oswald", sans-serif; color: var(--white); letter-spacing: 0.5px;
  }
  .features {
    position: absolute; left: 596px; top: 382px; list-style: none;
    font: 500 25px/38px "Ubuntu", sans-serif; color: var(--navy);
  }
  .brand {
    position: absolute; right: 40px; top: 420px; display: flex; align-items: center; gap: 12px;
  }
  .brand-dot { width: 30px; height: 30px; border-radius: 50%; background: var(--orange); }
  .brand-name { font: 700 26px/1 "Ubuntu", sans-serif; color: var(--navy); }
</style>
</head>
<body>
  <main class="sign">
    <div class="footer-band"></div>
    <div class="hero-photo" role="img" aria-label="Photo of a two-storey family home with green siding, lawn and driveway"></div>
    <p class="website">WWW.NORTHGATEHOMES.COM</p>
    <div class="agent">
      <p class="agent-name">Dana Whitfield, Listing Agent</p>
      <p class="agent-phone">555/014-2286</p>
    </div>

    <p class="sale-label">Home For Sale</p>
    <p class="price">$480,000</p>

    <div class="headline-band"></div>
    <h1 class="headline">Great Family Home Deal</h1>

    <div class="address-band"></div>
    <div class="thumbs">
      <div class="thumb thumb--living" role="img" aria-label="Living room interior photo"></div>
      <div class="thumb thumb--bedroom" role="img" aria-label="Bedroom interior photo"></div>
      <div class="thumb thumb--bath" role="img" aria-label="Bathroom interior photo"></div>
    </div>
    <h2 class="address">1418 LARKSPUR LANE</h2>

    <ul class="features">
      <li>4 Bedrooms</li>
      <li>3 Baths</li>
      <li>3200 Finished SF</li>
      <li>2 Car Garages</li>
    </ul>

    <div class="brand">
      <span class="brand-dot"></span>
      <span class="brand-name">Northgate Realty</span>
    </div>
  </main>
</body>
</html>
```